Website Design for Door Distributor

Garnet Door Design LLC distributes doors in the Southwestern region of the United States. We need a website design for our company launch.

We are looking for a website design that screams modern, and is easy to navigate. We want our customers to browse through our collections of doors with ease, while at the same time enjoy the feel of the website (more on how the website should feel below). Our logo is attached to help with the design process.

We expect this relationship to continue beyond the initial assignment, whether it includes additions or updates to the site. In that sense, we will only work with that designer who will specifically incorporate our ideas into the design, not a designer that submits a "one-size-fits-all" design. With that in mind, we are looking for a creative person who is willing to take some risks.

We are committed to minimizing the amount of revisions needed, so we encourage you to message us with any questions you may have throughout the process, especially in the earlier phases.

Thanks in advance for your time.

Target Market(s)

Home builders, commercial builders, developers, and upper-middle class/upper class customers. As you can see, our target market is of a more sophisticated type, so the design should be on the more serious side, and less playful. It should showcase a sense of class.

Industry/Entity Type

It Company

Requirements
Must have
• The home page should have a slideshow showcasing 4 to 5 different topics. See www.brivaleno.net for an example. The headings for each picture should be easily customizable (font, color, etc.). The user should also be able to click on the picture and be taken to the page that the pictures are linked to.

At the very top right of every page, there should be 2 header links: Download Brochure | Contact

There should be 5 static categories placed in one row at the top of each page. See www.tusk-ravo.com for an example. Each of these categories should drop down when you rest your mouse over it and display a list of links. Again, this should be easily customizable and shown on every page of the site. This will serve as the navigation menu. Let us know if you need to know the exact amount of links for each category - hopefully we can customize it on our end fairly easily.

Categories: Home | Products | Gallery | Support | About Us

Home Page: Along with the above, the home page should include a welcome section that introduces the user to the site. There should also be sections for "Featured Product" and "Testimonial".

Featured product: this will include an image and short text.

Testimonial: this will include a quote, which should be easy for us to update weekly, and a link to "More Testimonials".
Should not have
• No clutter - instead, the design layout should be open and easy to navigate.

No cartoonish graphics - instead, the graphics should be sophisticated and modern.

No flash, no java.

```html
<!DOCTYPE html>
<html lang="en">
<head>
<meta charset="utf-8">
<title>Garnet Door Design</title>
<link href="https://fonts.googleapis.com/css2?family=Open+Sans:wght@400;600&family=PT+Sans:ital@1&display=swap" rel="stylesheet">
<style>
:root{
  --brown:#6e3f18;
  --brown-dark:#4a2508;
  --nav-top:#93592a;
  --nav-bottom:#5e3413;
  --gold:#a2621f;
  --text:#555;
  --line:#d9d9d9;
  --footer:#303030;
}
*{margin:0;padding:0;box-sizing:border-box}
html,body{width:798px;height:1200px;overflow:hidden;background:#fff}
body{position:relative;font-family:"Open Sans",sans-serif;color:var(--text)}
.abs{position:absolute}
.brand{left:66px;top:60px;width:140px;text-align:center;color:var(--brown);font-size:22px;font-weight:400;line-height:24px;letter-spacing:1px}
.brand-mark{left:125px;top:14px;width:22px;height:40px;background:var(--brown)}
.top-links{right:68px;top:32px;font-size:10.5px;color:#444}
.top-links span{color:#aaa;margin:0 6px}
.call{right:98px;top:76px;text-align:right}
.call .label{font-size:13px;color:var(--gold)}
.call .phone{font-size:16px;color:var(--brown-dark);font-weight:600;line-height:18px}
.phone-icon{left:706px;top:84px}
.nav{left:0;top:146px;width:798px;height:34px;background:linear-gradient(var(--nav-top),var(--nav-bottom))}
.nav-item{top:0;height:34px;line-height:34px;color:#fff;font-size:11px;text-align:center;border-left:1px solid rgba(0,0,0,.25)}
.nav-item.active{background:var(--brown-dark)}
.search{left:586px;top:153px;width:144px;height:20px;background:#fff;border:1px solid #ccc;font-size:9.5px;color:#555;padding:3px 8px}
.search svg{position:absolute;right:6px;top:4px}
.hero{left:66px;top:190px;width:666px;height:314px;background:linear-gradient(90deg,#c9a56a,#8a5a32 35%,#6b3a1b 55%,#c8a26a 80%,#7c8a4a)}
.caption{left:66px;top:462px;width:666px;height:42px;background:rgba(20,20,20,.75);color:#fff;font-size:15px;line-height:42px;padding-left:20px}
.arrow-btn{top:476px;width:14px;height:14px;background:#fff;border:1px solid #999}
.dropdown{left:133px;top:180px;width:493px;height:102px;background:#4a2508}
.drop-panel{left:140px;top:186px;width:242px;height:92px;background:#fff;border-radius:3px}
.thumb{top:200px;width:18px;height:40px;background:linear-gradient(90deg,#f4f4f4,#d8d8d8)}
.thumb-label{top:257px;font-size:7px;color:#555;width:50px;text-align:center}
.drop-list{top:190px;list-style:none;font-size:8px;color:#e9dccd;line-height:13.8px}
.drop-list li:before{content:"• ";color:#fff}
h2{font-weight:400;color:var(--brown-dark);font-size:16px}
.welcome-title{left:69px;top:524px}
.welcome-text{left:69px;top:551px;width:490px;font-size:9.4px;line-height:16.8px}
.welcome-img{left:572px;top:528px;width:158px;height:102px;background:linear-gradient(135deg,#8a5a30,#5c3418)}
.divider{left:66px;top:658px;width:666px;height:1px;background:var(--line)}
.feat-title{left:68px;top:680px}
.card{width:152px;height:173px;border:1px solid var(--line);background:linear-gradient(#fff 70%,#f6f6f6);text-align:center}
.card .door{position:absolute;left:50%;top:12px;transform:translateX(-50%);width:52px;height:98px}
.card .name{position:absolute;top:126px;width:100%;font-size:9px;color:var(--gold)}
.card .desc{position:absolute;top:140px;width:100%;font-size:8px;line-height:11px;color:#777;padding:0 10px}
.testi-title{left:597px;top:680px}
.testi-box{left:572px;top:709px;width:158px;height:177px;border:1px solid var(--line)}
.quote{left:586px;top:724px;width:132px;font-family:"PT Sans",sans-serif;font-style:italic;font-size:9.5px;line-height:15.2px;color:#666;text-align:center}
.author{left:572px;top:838px;width:158px;text-align:center;font-size:9px;color:var(--brown-dark)}
.more{left:572px;top:865px;width:158px;height:21px;background:#e3e3e3;font-size:8.5px;line-height:21px;text-align:center;color:#555}
.comm-title{left:572px;top:902px}
.comm-box{left:572px;top:926px;width:158px;height:150px;border:1px solid var(--line)}
.member{width:30px;height:30px;background:linear-gradient(#b8b8b8,#7d7d7d)}
.member-name{width:40px;text-align:center;font-size:5px;color:#666}
.like{left:573px;top:1087px;width:30px;height:14px;border:1px solid #aab;background:#eef0f6;border-radius:2px}
.like-count{left:609px;top:1087px;width:16px;height:14px;border:1px solid #ccc;font-size:7px;text-align:center;line-height:12px;color:#555}
.page{top:1086px;width:17px;height:17px;border-radius:50%;background:#ddd;font-size:8px;line-height:17px;text-align:center;color:#666}
.page.current{background:var(--gold);color:#fff}
.footer{left:0;top:1132px;width:798px;height:68px;background:var(--footer)}
.footer-links{left:67px;top:1146px;font-size:8.8px;color:#ccc}
.copyright{left:67px;top:1171px;font-size:8.5px;color:#bbb}
.social{top:1157px;width:17px;height:17px;border-radius:50%;background:#6a6a6a}
</style>
</head>
<body>
<div class="abs brand-mark"></div>
<div class="abs brand">GARNET DOOR DESIGN</div>

<div class="abs top-links">Download Brochure<span>/</span>Contact</div>
<div class="abs call"><div class="label">Call us Today!</div><div class="phone">555 014 2290</div></div>
<svg class="abs phone-icon" width="24" height="18" viewBox="0 0 24 18"><path d="M2 6c0-4 20-4 20 0l-1 3h-4l-1-2H8L7 9H3z" fill="#4a2508"/><path d="M6 9h12l2 8H4z" fill="#4a2508"/><circle cx="12" cy="13" r="2.5" fill="#fff"/></svg>

<nav class="abs nav">
  <div class="abs nav-item" style="left:66px;width:67px">HOME</div>
  <div class="abs nav-item active" style="left:133px;width:92px">PRODUCTS</div>
  <div class="abs nav-item" style="left:225px;width:78px">GALLERY</div>
  <div class="abs nav-item" style="left:303px;width:82px">SUPPORT</div>
  <div class="abs nav-item" style="left:385px;width:85px;border-right:1px solid rgba(0,0,0,.25)">ABOUT US</div>
</nav>
<div class="abs search">Search<svg width="11" height="11" viewBox="0 0 11 11"><circle cx="4.5" cy="4.5" r="3.3" fill="none" stroke="#222" stroke-width="1.6"/><path d="M7 7l3.3 3.3" stroke="#222" stroke-width="2"/></svg></div>

<div class="abs hero" role="img" aria-label="Photo of a wooden double entry door with wrought iron glass panels between white columns and plants"></div>
<div class="abs caption">Nulla rutrum nulla id sollicitudin ultricies vestibulum convallis.</div>
<div class="abs arrow-btn" style="left:690px"><svg width="12" height="12"><path d="M7 3L4 6l3 3" stroke="#333" fill="none"/></svg></div>
<div class="abs arrow-btn" style="left:705px"><svg width="12" height="12"><path d="M5 3l3 3-3 3" stroke="#333" fill="none"/></svg></div>

<div class="abs dropdown"></div>
<div class="abs drop-panel"></div>
<div class="abs thumb" role="img" aria-label="All panel door" style="left:163px"></div>
<div class="abs thumb" role="img" aria-label="Glass panel door" style="left:223px"></div>
<div class="abs thumb" role="img" aria-label="Bifold door" style="left:285px"></div>
<div class="abs thumb" role="img" aria-label="Louver door" style="left:340px"></div>
<div class="abs thumb-label" style="left:147px">All Panel</div>
<div class="abs thumb-label" style="left:205px">Glass Panel</div>
<div class="abs thumb-label" style="left:269px">Bifold</div>
<div class="abs thumb-label" style="left:324px">Louver</div>
<ul class="abs drop-list" style="left:400px"><li>Integer lobortis</li><li>Curabitur ac</li><li>Phasellus tellus nisl</li><li>Aenean fringilla</li><li>Vestibulum</li><li>Aliquam commodo</li></ul>
<ul class="abs drop-list" style="left:520px"><li>Integer lobortis</li><li>Curabitur ac</li><li>Phasellus tellus nisl</li><li>Aenean fringilla</li><li>Vestibulum</li><li>Aliquam commodo</li></ul>

<h2 class="abs welcome-title">Welcome to Garnet Door Design</h2>
<p class="abs welcome-text">Nulla rutrum nulla id sollicitudin ultricies. Duis ut dolor metus. Nunc egestas est ac commodo ultricies. Morbi sollicitudin lobortis auctor. In hac habitasse platea dictumst. Integer vitae augue blandit, dapibus arcu in, vestibulum lacus. Nullam eu quam massa. Nullam facilisis nunc nec semper semper. Aliquam et suscipit erat, vitae iaculis libero. Curabitur sed dapibus nisl. Donec vel mauris ac purus dignissim dignissim non sit amet ligula. Donec ut nisl ut ligula iaculis fermentum at id enim. Mauris euismod lorem in felis lacinia.</p>
<div class="abs welcome-img" role="img" aria-label="Photo of a hand lifting a brass door knocker on a wooden door"></div>
<div class="abs divider"></div>

<h2 class="abs feat-title">Featured Product</h2>
<svg class="abs" style="left:541px;top:685px" width="18" height="10"><path d="M5 1L1 5l4 4M13 1l4 4-4 4" stroke="#555" stroke-width="1.6" fill="none"/></svg>

<div class="abs card" style="left:69px;top:709px"><div class="door" role="img" aria-label="Honey oak panel door" style="background:linear-gradient(90deg,#d58a3c,#a85a20)"></div><div class="name">Donec vel mauris</div><div class="desc">Nam vitae tellus tristique, sceleri sque quam eget, egestas dolor.</div></div>
<div class="abs card" style="left:237px;top:709px"><div class="door" role="img" aria-label="Red mahogany carved door" style="background:linear-gradient(90deg,#9a2a18,#6e1a0e)"></div><div class="name">Donec vel mauris</div><div class="desc">Nam vitae tellus tristique, sceleri sque quam eget, egestas dolor.</div></div>
<div class="abs card" style="left:405px;top:709px"><div class="door" role="img" aria-label="White six panel door" style="background:linear-gradient(90deg,#f6f6f6,#dcdcdc);border:1px solid #ccc"></div><div class="name">Donec vel mauris</div><div class="desc">Nam vitae tellus tristique, sceleri sque quam eget, egestas dolor.</div></div>
<div class="abs card" style="left:69px;top:897px"><div class="door" role="img" aria-label="Light wood arched panel door" style="background:linear-gradient(90deg,#c97a2e,#9e561a)"></div><div class="name">Donec vel mauris</div><div class="desc">Nam vitae tellus tristique, sceleri sque quam eget, egestas dolor.</div></div>
<div class="abs card" style="left:237px;top:897px"><div class="door" role="img" aria-label="Gothic arched wooden door" style="background:linear-gradient(90deg,#a8672c,#6a3c16);border-radius:26px 26px 0 0"></div><div class="name">Donec vel mauris</div><div class="desc">Nam vitae tellus tristique, sceleri sque quam eget, egestas dolor.</div></div>
<div class="abs card" style="left:405px;top:897px"><div class="door" role="img" aria-label="Dark walnut modern door" style="background:linear-gradient(90deg,#5a3420,#3a2012);width:40px;height:92px"></div><div class="name">Donec vel mauris</div><div class="desc">Nam vitae tellus tristique, sceleri sque quam eget, egestas dolor.</div></div>

<svg class="abs" style="left:573px;top:681px" width="20" height="17"><ellipse cx="10" cy="7" rx="9.5" ry="6.5" fill="#4a2508"/><path d="M4 11l-2 5 6-3z" fill="#4a2508"/></svg>
<h2 class="abs testi-title">Testimonials</h2>
<div class="abs testi-box"></div>
<p class="abs quote"><b style="font-size:13px;color:#555">“</b> Donec at tempus lectus, eget condimentum neque. Sed commodo eleifend scelerisque. Nunc risus quam, accumsan eu mauris eu, lacinia tincidunt metus. Class aptent taciti sociosqu ad litora <b style="font-size:13px;color:#555">”</b></p>
<div class="abs author">Martin Hale, City</div>
<div class="abs more">More Testimonials</div>

<h2 class="abs comm-title">Community</h2>
<div class="abs comm-box"></div>
<div class="abs member" role="img" aria-label="Member photo" style="left:578px;top:933px"></div>
<div class="abs member" role="img" aria-label="Member photo" style="left:617px;top:933px"></div>
<div class="abs member" role="img" aria-label="Member photo" style="left:656px;top:933px"></div>
<div class="abs member" role="img" aria-label="Member photo" style="left:695px;top:933px"></div>
<div class="abs member" role="img" aria-label="Member photo" style="left:578px;top:980px"></div>
<div class="abs member" role="img" aria-label="Member photo" style="left:617px;top:980px"></div>
<div class="abs member" role="img" aria-label="Member photo" style="left:656px;top:980px"></div>
<div class="abs member" role="img" aria-label="Member photo" style="left:695px;top:980px"></div>
<div class="abs member" role="img" aria-label="Member photo" style="left:578px;top:1028px"></div>
<div class="abs member" role="img" aria-label="Member photo" style="left:617px;top:1028px"></div>
<div class="abs member-name" style="left:573px;top:968px">Alina</div>
<div class="abs member-name" style="left:612px;top:968px">Tomas</div>
<div class="abs member-name" style="left:651px;top:968px">Vero</div>
<div class="abs member-name" style="left:690px;top:968px">Dorian</div>
<div class="abs member-name" style="left:573px;top:1015px">Lenka</div>
<div class="abs member-name" style="left:612px;top:1015px">Rami</div>
<div class="abs member-name" style="left:651px;top:1015px">Suda</div>
<div class="abs member-name" style="left:690px;top:1015px">Hadi</div>
<div class="abs member-name" style="left:573px;top:1064px">Ilse</div>
<div class="abs member-name" style="left:612px;top:1064px">Yusuf</div>
<div class="abs like"></div>
<div class="abs like-count">3k</div>

<div class="abs page" style="left:435px">«</div>
<div class="abs page current" style="left:456px">1</div>
<div class="abs page" style="left:477px">2</div>
<div class="abs page" style="left:498px">3</div>
<div class="abs page" style="left:519px">4</div>
<div class="abs page" style="left:540px">»</div>

<footer class="abs footer"></footer>
<div class="abs footer-links">Home | Products | Gallery | Support | About Us | Download Brochure | Contact</div>
<div class="abs copyright">Copyright © 2013 Garnet Door Design. All rights reserved.</div>
<div class="abs social" style="left:645px"></div>
<div class="abs social" style="left:668px"></div>
<div class="abs social" style="left:691px"></div>
<div class="abs social" style="left:714px"></div>
</body>
</html>
```